Thorne Legal PC business card. National Consumer Law Firm with principal office in San Francisco. We maintain additional offices in Meridian, Mississippi and Birmingham, Alabama. We protect consumers against unscrupulous mega corporations. We want to covey integrity and a willingness to take on the Goliaths of the corporate world. I like red accents. Try to use uploaded picture of Harbor Arch Span or a sketch. Licensed in California, Alabama and Mississippi. Main office: 318 Alder Ave. #407, San Francisco, CA 94110, ph. 415/555-0182, 800/555-0147 (fax), 205/555-0136 (AL).
www.thornelegalpc.example
www.claimwatch.example.
At top--Public Claim Advocacy in red. Also Thorne Legal PC at top in red. Then red horizontal line please. Or if you have another idea. I have not seen new logo.
After line on left at top
H. Dwight Thorne
Attorney
Cell 205/555-0194
dwight@thornelegalpc.example
Offices: San Francisco, CA, Birmingham, AL, Charlotte, NC and Meridian, MS

I asked that the very bottom of the BUSINESS CARD TO SAY "Offices in California, North Carolina, Alabama and Mississippi NOT STATES WHERE I AM LICENSED. I.E., I AM NOT LICENSED IN NOTH CAROLINA I NEED NEW FILES IF YOU CAN GET THEM IN THE MORNING MY TIME. WHERE CAN I FIND THE NEW FILES ONCE YOU MODIFY.

for North Carolina, I need an asterick where it is listed. "not licensed will associate counsel" AGAIN NORTH CAROLINA IS 2 WORDS WITH A SPACE BETWEEN THEM

For Biz card, put tollfree number (888)555-0129 and toll free fax (800)555-0147 somewhere like below my cell number or wherever you can. States where I have offices at the bottom: California, North Carolina, Alabama and Mississippi.

For Biz card, put tollfree number (888)555-0129 and toll free fax (800)555-0147 somewhere like below my cell number or wherever you can. States where I have offices at the bottom: California, North Carolina, Alabama and Mississippi. AstericK *North Carolina--not licensed will associate co-counel. Same with letterhead and website. I need to disclose not licensed to practice in North Carolina.

```html
<!DOCTYPE html>
<html lang="en">
<head>
<meta charset="utf-8">
<title>Thorne Legal PC — Business Card</title>
<link rel="stylesheet" href="https://fonts.googleapis.com/css2?family=Oxygen:wght@300;400;700&display=swap">
<style>
  :root {
    --page: #ffffff;
    --olive-top: #807c63;
    --olive-mid: #6a664f;
    --olive-deep: #3d392b;
    --band-red: rgba(236, 70, 48, 0.96);
    --strip-red: #cb3027;
    --accent-red: #d8352c;
    --ink-light: #ffffff;
    --ink-soft: #e4e0d2;
  }
  * { box-sizing: border-box; margin: 0; padding: 0; }
  html, body {
    width: 1200px; height: 1000px; overflow: hidden;
    background: var(--page);
    font-family: "Oxygen", Arial, sans-serif;
  }
  .card {
    position: absolute; left: 252px; top: 261px;
    width: 727px; height: 411px; overflow: hidden;
    color: var(--ink-light);
  }
  .card__photo {
    position: absolute; inset: 0;
    background: linear-gradient(180deg, var(--olive-top) 0%, var(--olive-mid) 55%, var(--olive-deep) 100%);
  }
  .card__practice {
    position: absolute; top: 16px; left: 0; width: 100%;
    text-align: center; font-size: 32px; font-weight: 700;
    letter-spacing: 2.4px; padding-left: 10px;
  }
  .card__brand-band {
    position: absolute; top: 62px; left: 0; width: 100%; height: 100px;
    background: var(--band-red);
    display: flex; align-items: center; justify-content: center;
  }
  .brand-name {
    font-weight: 300; font-size: 52px; letter-spacing: 1px;
    color: var(--ink-light); padding-left: 30px;
  }
  .contact-person {
    position: absolute; left: 71px; top: 180px;
  }
  .contact-person__name { font-size: 19px; font-weight: 700; letter-spacing: 0.8px; }
  .contact-person__title { font-size: 16px; color: var(--accent-red); letter-spacing: 0.8px; margin-bottom: 10px; }
  .contact-line { font-size: 16px; letter-spacing: 0.9px; line-height: 24px; white-space: nowrap; }
  .contact-line .label { color: var(--accent-red); }
  .office {
    position: absolute; right: 76px; top: 181px; text-align: right;
  }
  .card__web-strip {
    position: absolute; top: 320px; left: 0; width: 100%; height: 27px;
    background: var(--strip-red);
    display: flex; align-items: center; justify-content: center;
    font-size: 17px; letter-spacing: 2px; gap: 20px; padding-left: 8px;
  }
  .card__offices {
    position: absolute; top: 357px; left: 0; width: 100%;
    text-align: center; font-size: 13px; font-weight: 700; letter-spacing: 1.8px;
    white-space: nowrap;
  }
  .card__offices .mark { color: var(--accent-red); }
  .card__disclaimer {
    position: absolute; top: 381px; left: 0; width: 100%;
    text-align: center; font-size: 11px; letter-spacing: 1px;
    color: var(--ink-soft);
  }
  .card__disclaimer .mark { color: var(--accent-red); }
</style>
</head>
<body>
  <div class="card">
    <div class="card__photo" role="img" aria-label="Sepia-toned photograph of the Harbor Arch Span over the bay"></div>

    <div class="card__practice">PUBLIC CLAIM ADVOCACY</div>

    <div class="card__brand-band">
      <span class="brand-name">THORNE LEGAL PC</span>
    </div>

    <div class="contact-person">
      <div class="contact-person__name">H. Dwight Thorne</div>
      <div class="contact-person__title">Attorney</div>
      <div class="contact-line">205/555-0194 <span class="label">(cell)</span></div>
      <div class="contact-line">(888)555-0129 <span class="label">(toll free)</span></div>
      <div class="contact-line">dwight@thornelegalpc.example</div>
    </div>

    <div class="office">
      <div class="contact-line">318 Alder Ave. #407</div>
      <div class="contact-line">San Francisco, CA 94110</div>
      <div class="contact-line">415/555-0182 <span class="label">(CA)</span></div>
      <div class="contact-line">800/555-0147 <span class="label">(toll free fax)</span></div>
      <div class="contact-line">205/555-0136 <span class="label">(AL)</span></div>
    </div>

    <div class="card__web-strip">
      <span>www.thornelegalpc.example</span>
      <span>|</span>
      <span>www.claimwatch.example</span>
    </div>

    <div class="card__offices">OFFICES IN CALIFORNIA, NORTH CAROLINA<span class="mark">*</span>, ALABAMA AND MISSISSIPPI</div>
    <div class="card__disclaimer"><span class="mark">*</span>North Carolina: not licensed, will associate co-counsel</div>
  </div>
</body>
</html>
```